Card for modern wood artisan that builds log homes and timber frames.

Design a card with catchy imagery. With a quick list of things I build and services I offer.

I'd like an English side and a french side. I can provide the text.

I am basically a guy that builds log homes and timber frames , but I am very eco friendly oriented.

I use only eco friendly products to limit my carbon footprint.
I want the client to feel as if they are hiring a good smart builder.

I have been building for a while but just starting out to market myself out there , not just work for other companies. Starting
My own thing legitimately.

I am very conscientious, and I take care of the work I do. I am trying to bring a new age, modern feel to an old profession.

Reason: I am not completely satisfied with A model yet, looking for that masculin rustic artistic design that I havent completely found yet. Thank you for your sumbissions.

Target Market(s)

People looking to hire a builder to design and build their projects.
And contractors that want to hire a quality subcontractor for their jobs.

Industry/Entity Type

Construction

Contact Information for Business Card

I want my logo on it, that I had designed here.
And a list of services I provide.

With my phone number, website adress and Email.

Requirements
Must have
• Artful presentation,
• Eco friendly feel
• I love trees.

```html
<!DOCTYPE html>
<html lang="en">
<head>
<meta charset="UTF-8">
<title>Orleva – Wood Artisan Card</title>
<link rel="stylesheet" href="https://fonts.googleapis.com/css2?family=Bebas+Neue&family=Oswald:wght@500&family=Open+Sans:wght@500&display=swap">
<style>
  :root {
    --backdrop: #c8ccce;
    --kraft: #b59c74;
    --kraft-dark: #a58a5f;
    --ink: #1f1612;
  }
  * { margin: 0; padding: 0; box-sizing: border-box; }
  html, body {
    width: 778px;
    height: 1200px;
    overflow: hidden;
    background: var(--backdrop);
  }
  .card {
    position: absolute;
    left: 99px;
    top: 83px;
    width: 580px;
    height: 1034px;
    background: var(--kraft);
    color: var(--ink);
  }
  .wood-stain {
    position: absolute;
    left: 300px;
    top: 360px;
    width: 250px;
    height: 680px;
    background: radial-gradient(ellipse at 50% 45%, rgba(150,118,72,0.55) 0%, rgba(150,118,72,0.25) 45%, rgba(150,118,72,0) 70%);
  }
  .brand-frame {
    position: absolute;
    left: 53px;
    top: 65px;
    width: 473px;
    height: 102px;
    border: 3px solid var(--ink);
    padding: 5px;
  }
  .brand-block {
    display: flex;
    align-items: center;
    height: 100%;
    background: var(--ink);
    color: var(--kraft);
  }
  .brand-mark {
    width: 52px;
    height: 52px;
    margin: 0 34px 0 28px;
    background: var(--kraft);
  }
  .brand-divider {
    width: 4px;
    height: 100%;
    background: var(--kraft);
    margin-right: 34px;
  }
  .brand-name {
    font-family: 'Oswald', sans-serif;
    font-weight: 500;
    font-size: 62px;
    letter-spacing: 3px;
    line-height: 1;
  }
  .tagline {
    position: absolute;
    top: 210px;
    left: 0;
    width: 100%;
    text-align: center;
    font-family: 'Oswald', sans-serif;
    font-weight: 500;
    font-size: 36px;
    letter-spacing: 1px;
  }
  .rule-dashed {
    position: absolute;
    left: 50px;
    top: 365px;
    width: 485px;
    border-top: 2px dashed var(--ink);
    opacity: 0.8;
  }
  .services {
    position: absolute;
    left: 50px;
    top: 420px;
    width: 480px;
    list-style: none;
    font-family: 'Bebas Neue', sans-serif;
    font-size: 58px;
    line-height: 53px;
  }
  .services li {
    display: flex;
    justify-content: space-between;
    align-items: baseline;
  }
  .services .amp {
    font-family: Georgia, serif;
    font-style: italic;
    font-size: 44px;
    opacity: 0.7;
  }
  .rule-solid {
    position: absolute;
    left: 50px;
    top: 792px;
    width: 480px;
    border-top: 4px solid var(--ink);
  }
  .contact {
    position: absolute;
    top: 850px;
    left: 0;
    width: 100%;
    text-align: center;
    font-family: 'Open Sans', sans-serif;
    font-weight: 500;
    font-size: 28px;
    line-height: 39px;
    letter-spacing: 2px;
  }
</style>
</head>
<body>
  <div class="card">
    <div class="wood-stain" role="img" aria-label="Faint wood grain stain texture"></div>

    <div class="brand-frame">
      <div class="brand-block">
        <div class="brand-mark"></div>
        <div class="brand-divider"></div>
        <span class="brand-name">ORLEVA</span>
      </div>
    </div>

    <p class="tagline">WOOD ARTISAN</p>
    <div class="rule-dashed"></div>

    <ul class="services">
      <li aria-label="Carpentry"><span>C</span><span>A</span><span>R</span><span>P</span><span>E</span><span>N</span><span>T</span><span>R</span><span>Y</span></li>
      <li aria-label="Log homes"><span>L</span><span>O</span><span>G</span><span>&nbsp;</span><span>H</span><span>O</span><span>M</span><span>E</span><span>S</span></li>
      <li aria-label="Timber frames"><span>T</span><span>I</span><span>M</span><span>B</span><span>E</span><span>R</span><span>&nbsp;</span><span>F</span><span>R</span><span>A</span><span>M</span><span>E</span><span>S</span></li>
      <li aria-label="Stairs and ramps"><span>S</span><span>T</span><span>A</span><span>I</span><span>R</span><span>S</span><span class="amp">&amp;</span><span>R</span><span>A</span><span>M</span><span>P</span><span>S</span></li>
      <li aria-label="Wood stuff"><span>W</span><span>O</span><span>O</span><span>D</span><span>&nbsp;</span><span>S</span><span>T</span><span>U</span><span>F</span><span>F</span></li>
      <li aria-label="For the home"><span>F</span><span>O</span><span>R</span><span>&nbsp;</span><span>T</span><span>H</span><span>E</span><span>&nbsp;</span><span>H</span><span>O</span><span>M</span><span>E</span></li>
    </ul>

    <div class="rule-solid"></div>

    <div class="contact">
      <p>555.014.2270</p>
      <p>mark@orleva.com</p>
      <p>www.orleva.com</p>
    </div>
  </div>
</body>
</html>
```